Business Card Design using new logo

As much as we'd like to think that treating everyone equally is the best strategy for fairness, the reality is that the differences in the lives of women and men have to be taken into account to ensure that organizations, programs, services, and yes, even public policy treat women and men in ways that achieve gender equity.

That's where ParityLoom - balance insight metrics comes in. Using the data-driven tools of gender analysis, our organization can help anyone determine if gender equity is being achieved - in businesses and organizations, in the planning and implementation of programs and services, and in the development and enforcement of public policy.
Updates

Apologies for the delay - have not had time to finalize the decision.  Should be early this week - probably Tuesday.

Industry/Entity Type

Business

Requirements
Must have
• New Logo for ParityLoom
• Logo plus words "Balance Insight Metrics"

```html
<!DOCTYPE html>
<html lang="en">
<head>
<meta charset="utf-8">
<title>ParityLoom Business Cards</title>
<link rel="stylesheet" href="https://fonts.googleapis.com/css2?family=Raleway:wght@300;400;600&display=swap">
<style>
  :root {
    --backdrop: #2b2b2d;
    --card: #f4f4f2;
    --ink: #2f2f2f;
    --ink-soft: #555555;
    --accent: #e8871e;
    --muted: #9a9a9a;
  }
  * { box-sizing: border-box; margin: 0; padding: 0; }
  html, body {
    width: 1200px;
    height: 996px;
    overflow: hidden;
    background: var(--backdrop);
  }
  .stage {
    position: relative;
    width: 1200px;
    height: 996px;
  }
  .card {
    position: absolute;
    left: 250px;
    width: 700px;
    height: 400px;
    background: var(--card);
    font-family: "Raleway", Arial, sans-serif;
    color: var(--ink);
  }
  .card--front { top: 70px; }
  .card--back { top: 526px; }

  /* Front */
  .front-brand {
    position: absolute;
    left: 60px;
    top: 95px;
    display: flex;
    align-items: center;
    gap: 26px;
  }
  .brand-dot {
    width: 92px;
    height: 92px;
    border-radius: 50%;
    background: var(--accent);
    flex: none;
  }
  .brand-name {
    font-weight: 600;
    font-size: 72px;
    line-height: 1;
    color: var(--ink);
    letter-spacing: -0.5px;
  }
  .front-tagline {
    position: absolute;
    right: 56px;
    top: 200px;
    font-weight: 400;
    font-size: 34px;
    color: var(--ink-soft);
  }

  /* Back */
  .back-name {
    position: absolute;
    left: 240px;
    top: 40px;
    font-weight: 600;
    font-size: 56px;
    line-height: 1;
  }
  .back-dot {
    position: absolute;
    left: 70px;
    top: 120px;
    width: 120px;
    height: 120px;
    border-radius: 50%;
    background: var(--accent);
  }
  .contact {
    position: absolute;
    left: 240px;
    top: 115px;
    font-weight: 300;
    color: var(--ink-soft);
    font-size: 22px;
    line-height: 1.3;
  }
  .contact .person { font-size: 30px; font-weight: 400; color: var(--ink); }
  .contact .role { font-size: 24px; margin-bottom: 8px; }
  .contact .gap { height: 10px; }
  .back-tagline {
    position: absolute;
    left: 240px;
    bottom: 34px;
    font-weight: 300;
    font-size: 30px;
    color: var(--ink-soft);
  }
</style>
</head>
<body>
<main class="stage">
  <section class="card card--front" aria-label="Business card front">
    <div class="front-brand">
      <span class="brand-dot" aria-hidden="true"></span>
      <span class="brand-name">ParityLoom</span>
    </div>
    <p class="front-tagline">Balance Insight Metrics</p>
  </section>

  <section class="card card--back" aria-label="Business card back">
    <p class="back-name">ParityLoom</p>
    <span class="back-dot" aria-hidden="true"></span>
    <div class="contact">
      <p class="person">Maren Ostrow</p>
      <p class="role">Prime Analyst</p>
      <p>o.&nbsp; 555. 014. 2200</p>
      <p>m. 555. 014. 2209</p>
      <div class="gap"></div>
      <p>e. marenostrow@parityloom.com</p>
      <p>w. www.parityloom.com</p>
    </div>
    <p class="back-tagline">Balance Insight Metrics</p>
  </section>
</main>
</body>
</html>
```